Tovrine brothers artist graphic

A album type cover/band logo to be used on spotify, itunes etc. 3000 x 3000 is the preferred spec. Tovrine Brothers is a country style music group. Sounds like Herons/Paul Dexter/Pale Harbours. My favourite reference artwork would be:Paul Dexter - Cut and Gathered album cover.Restive Nolan - Good Luck True LoveLori Mckenna - The Bird and The RifleMust have the words 'Tovrine Brothers' on it.

Logo Text

Tovrine Brothers

Colors

Designer to choose colors to be used in the design.

Requirements
Must have
• The colour wheel below doesn't really work for me!
• Colours can be chosen based not the album references I have put in the description

```html
<!DOCTYPE html>
<html lang="en">
<head>
<meta charset="utf-8">
<title>Tovrine Brothers</title>
<link rel="stylesheet" href="https://fonts.googleapis.com/css2?family=Kaushan+Script&display=block">
<style>
  :root {
    --sky-deep: #1a1219;
    --sky-brown: #2e1c1c;
    --cloud-rust: #5a2e1e;
    --horizon-copper: #a1552a;
    --water-amber: #d9843e;
    --sun-glow: #f3c47a;
    --title-white: #ffffff;
  }
  html, body {
    margin: 0;
    padding: 0;
    width: 1200px;
    height: 1200px;
    overflow: hidden;
    background: var(--sky-deep);
  }
  .cover {
    position: relative;
    width: 1200px;
    height: 1200px;
    overflow: hidden;
  }
  .cover__scene,
  .cover__swash {
    position: absolute;
    inset: 0;
    width: 1200px;
    height: 1200px;
    display: block;
  }
  .cover__title {
    margin: 0;
    font-family: "Kaushan Script", "Brush Script MT", cursive;
    font-weight: 400;
    color: var(--title-white);
  }
  .cover__title-line {
    position: absolute;
    display: block;
    white-space: nowrap;
    line-height: 1;
    font-size: 225px;
    transform: translate(-50%, -50%) rotate(-15deg);
  }
  .cover__title-line--first {
    left: 610px;
    top: 400px;
  }
  .cover__title-line--second {
    left: 600px;
    top: 590px;
  }
</style>
</head>
<body>
  <main class="cover">
    <svg class="cover__scene" viewBox="0 0 1200 1200" role="img" aria-label="Posterized photograph of a sunset over water, dark clouded sky above a glowing amber horizon and reflections">
      <defs>
        <linearGradient id="sky-to-water" x1="0" y1="0" x2="0" y2="1">
          <stop offset="0" stop-color="var(--sky-deep)"/>
          <stop offset="0.4" stop-color="var(--sky-brown)"/>
          <stop offset="0.62" stop-color="var(--cloud-rust)"/>
          <stop offset="0.75" stop-color="var(--horizon-copper)"/>
          <stop offset="1" stop-color="var(--cloud-rust)"/>
        </linearGradient>
        <radialGradient id="sun-reflection" cx="0.55" cy="0.85" r="0.4">
          <stop offset="0" stop-color="var(--sun-glow)" stop-opacity="0.75"/>
          <stop offset="0.5" stop-color="var(--water-amber)" stop-opacity="0.45"/>
          <stop offset="1" stop-color="var(--water-amber)" stop-opacity="0"/>
        </radialGradient>
      </defs>
      <rect width="1200" height="1200" fill="url(#sky-to-water)"/>
      <rect width="1200" height="1200" fill="url(#sun-reflection)"/>
    </svg>

    <svg class="cover__swash" viewBox="0 0 1200 1200" role="img" aria-label="White calligraphic swash flourish looping beneath the band name">
      <defs>
        <radialGradient id="swash-glow" cx="0.5" cy="0.5" r="0.5">
          <stop offset="0" stop-color="var(--title-white)" stop-opacity="0.28"/>
          <stop offset="1" stop-color="var(--title-white)" stop-opacity="0"/>
        </radialGradient>
      </defs>
      <ellipse cx="650" cy="820" rx="400" ry="110" transform="rotate(-8 650 820)" fill="url(#swash-glow)"/>
    </svg>

    <h1 class="cover__title">
      <span class="cover__title-line cover__title-line--first">Tovrine</span>
      <span class="cover__title-line cover__title-line--second">Brothers</span>
    </h1>
  </main>
</body>
</html>
```